Maple Grin
Pediatric and Family Dentistry
Maple Grin -
Creative Brief
Bright & Fun-filled
Doria Velcott, DMD
Pediatric Dentist
1746 Brannock Lane, Suite 410 Fairfax, VA 22157
maplegrinoffice@brindlemail.com
MapleGrinClinic.com
We would like a second name on this card as listed below Name: Lorna Tevick, DDS Title: General Dentist
Appointment For: Date: Time:

```html
<!DOCTYPE html>
<html lang="en">
<head>
<meta charset="utf-8">
<title>Maple Grin Stationery</title>
<link href="https://fonts.googleapis.com/css2?family=Nunito:wght@400;700;800&display=swap" rel="stylesheet">
<style>
:root{
  --bg:#5c5c5c;
  --paper:#ffffff;
  --ink:#1b1b1b;
  --orange:#f38a1d;
  --orange-light:#f9b25a;
  --muted:#8a8a8a;
  --wordmark:#f38a1d;
}
*{margin:0;padding:0;box-sizing:border-box}
html,body{width:1200px;height:302px;overflow:hidden}
body{background:var(--bg);font-family:"Nunito",sans-serif;position:relative;color:var(--ink)}
.sheet{position:absolute;background:var(--paper);overflow:hidden;box-shadow:0 1px 3px rgba(0,0,0,.35)}
.brand{display:flex;align-items:center;gap:4px}
.brand .dot{border-radius:50%;background:var(--orange);flex:none}
.brand .name{font-weight:800;color:var(--wordmark);line-height:1;white-space:nowrap}
.tagline{color:var(--ink);font-weight:700;white-space:nowrap}
.set-title{position:absolute;left:24px;top:24px}
.set-title .dot{width:22px;height:22px}
.set-title .name{font-size:30px;color:#fff}
.set-sub{position:absolute;left:52px;top:60px;font-size:10px;color:#fff;font-weight:700}
.set-note{position:absolute;left:24px;top:100px;font-size:7px;color:#ddd}
.wave{position:absolute;left:0;bottom:0;width:100%}
.fine{font-size:4px;line-height:1.45;color:var(--muted)}
/* business cards */
.card{width:98px;height:58px}
.card .brand{position:absolute;left:7px;top:8px}
.card .dot{width:9px;height:9px}
.card .name{font-size:12px}
.card .tagline{position:absolute;left:20px;top:21px;font-size:4px}
.card.dark{background:var(--ink)}
.card.dark .fine{color:#ccc}
.card .person{position:absolute;left:8px;top:9px;font-size:5px;font-weight:800;color:#fff}
.card .role{font-weight:400;color:var(--orange)}
.card .details{position:absolute;left:8px;top:28px}
.card .appt{position:absolute;left:8px;top:8px;font-size:4.5px;line-height:2.2;color:var(--ink);font-weight:700}
.card .appt span{display:inline-block;width:60px;border-bottom:.5px solid var(--muted);margin-left:3px}
/* letterhead */
.letter{width:202px;height:276px;top:12px}
.letter .brand{position:absolute;left:14px;top:14px}
.letter .dot{width:12px;height:12px}
.letter .name{font-size:15px}
.letter .tagline{position:absolute;left:31px;top:31px;font-size:5px}
.letter .contact{position:absolute;left:122px;top:14px}
/* compliment slip and envelopes */
.slip{left:712px;top:12px;width:146px;height:120px}
.slip .brand{position:absolute;left:10px;top:10px}
.slip .dot{width:10px;height:10px}
.slip .name{font-size:12px}
.small-env{left:712px;top:172px;width:148px;height:112px}
.small-env .brand{position:absolute;left:10px;top:10px}
.small-env .dot{width:8px;height:8px}
.small-env .name{font-size:10px}
.env-back{left:876px;top:12px;width:314px;height:110px;background:none;box-shadow:none}
.env-dl{width:314px;height:78px}
.env-dl .brand{position:absolute;left:12px;top:10px}
.env-dl .dot{width:8px;height:8px}
.env-dl .name{font-size:11px}
.env-dl .return{position:absolute;left:12px;top:24px}
</style>
</head>
<body>

<header>
  <div class="set-title brand"><span class="dot"></span><span class="name">Maple Grin</span></div>
  <p class="set-sub">Pediatric and Family Dentistry</p>
  <p class="set-note">Stationery Set</p>
</header>

<!-- business cards -->
<section class="sheet card" style="left:12px;top:120px">
  <div class="brand"><span class="dot"></span><span class="name">Maple Grin</span></div>
  <p class="tagline">Pediatric and Family Dentistry</p>
  <svg class="wave" viewBox="0 0 100 20" preserveAspectRatio="none" height="12"><path d="M0 14 Q50 4 100 10 L100 20 L0 20Z" fill="var(--orange)"/><path d="M0 12 Q50 2 100 8" stroke="var(--ink)" stroke-width="1.2" fill="none"/></svg>
</section>

<section class="sheet card dark" style="left:120px;top:120px">
  <p class="person">Doria Velcott, DMD <span class="role">Pediatric Dentist</span><br>Lorna Tevick, DDS <span class="role">General Dentist</span></p>
  <div class="details fine">1746 Brannock Lane, Suite 410 Fairfax, VA 22157<br>Tel 703.555.0142<br>maplegrinoffice@brindlemail.com<br>MapleGrinClinic.com</div>
</section>

<section class="sheet card" style="left:12px;top:204px">
  <div class="brand"><span class="dot"></span><span class="name">Maple Grin</span></div>
  <p class="tagline">Pediatric and Family Dentistry</p>
  <svg class="wave" viewBox="0 0 100 20" preserveAspectRatio="none" height="12"><path d="M0 14 Q50 4 100 10 L100 20 L0 20Z" fill="var(--orange)"/><path d="M0 12 Q50 2 100 8" stroke="var(--ink)" stroke-width="1.2" fill="none"/></svg>
</section>

<section class="sheet card" style="left:120px;top:204px">
  <p class="appt">Appointment For:<span></span><br>Date:<span></span><br>Time:<span></span></p>
  <svg class="wave" viewBox="0 0 100 20" preserveAspectRatio="none" height="20"><path d="M0 6 Q50 18 100 4 L100 20 L0 20Z" fill="var(--orange)"/></svg>
  <p class="fine" style="position:absolute;left:8px;bottom:3px;color:#fff">Tel 703.555.0142</p>
</section>

<!-- letterheads -->
<section class="sheet letter" style="left:260px">
  <div class="brand"><span class="dot"></span><span class="name">Maple Grin</span></div>
  <p class="tagline">Pediatric and Family Dentistry</p>
  <div class="contact fine">1746 Brannock Lane, Suite 410<br>Fairfax, VA 22157<br>Tel 703.555.0142<br>maplegrinoffice@brindlemail.com<br>MapleGrinClinic.com</div>
  <svg class="wave" viewBox="0 0 200 40" preserveAspectRatio="none" height="30"><path d="M0 30 Q100 8 200 22 L200 40 L0 40Z" fill="var(--orange)"/><path d="M0 26 Q100 4 200 18" stroke="var(--ink)" stroke-width="3" fill="none"/></svg>
</section>

<section class="sheet letter" style="left:500px">
  <div class="brand"><span class="dot"></span><span class="name">Maple Grin</span></div>
  <p class="tagline">Pediatric and Family Dentistry</p>
  <div class="contact fine">1746 Brannock Lane, Suite 410<br>Fairfax, VA 22157<br>Tel 703.555.0142<br>maplegrinoffice@brindlemail.com<br>MapleGrinClinic.com</div>
  <svg class="wave" viewBox="0 0 200 40" preserveAspectRatio="none" height="30"><path d="M0 30 Q100 8 200 22 L200 40 L0 40Z" fill="var(--orange)"/><path d="M0 26 Q100 4 200 18" stroke="var(--ink)" stroke-width="3" fill="none"/></svg>
</section>

<!-- compliment slip -->
<section class="sheet slip">
  <div class="brand"><span class="dot"></span><span class="name">Maple Grin</span></div>
  <svg class="wave" viewBox="0 0 200 40" preserveAspectRatio="none" height="22"><path d="M0 30 Q100 8 200 22 L200 40 L0 40Z" fill="var(--orange)"/><path d="M0 26 Q100 4 200 18" stroke="var(--ink)" stroke-width="3" fill="none"/></svg>
</section>

<!-- small envelope -->
<section class="sheet small-env">
  <div class="brand"><span class="dot"></span><span class="name">Maple Grin</span></div>
  <svg class="wave" viewBox="0 0 200 40" preserveAspectRatio="none" height="40"><path d="M0 18 Q100 2 200 14 L200 40 L0 40Z" fill="var(--orange)"/><path d="M0 14 Q100 -2 200 10" stroke="var(--ink)" stroke-width="3" fill="none"/></svg>
</section>

<!-- envelope backs -->
<section class="sheet env-back">
  <svg viewBox="0 0 314 110" width="314" height="110">
    <path d="M0 0 H314 V70 L157 20 L0 70Z" fill="var(--ink)"/>
    <path d="M0 70 L157 20 L314 70 V110 H0Z" fill="var(--orange)"/>
    <path d="M0 95 L157 50 L314 95 V110 H0Z" fill="var(--orange-light)"/>
  </svg>
</section>

<section class="sheet env-dl" style="left:876px;top:132px">
  <div class="brand"><span class="dot"></span><span class="name">Maple Grin</span></div>
  <div class="return fine">1746 Brannock Lane, Suite 410<br>Fairfax, VA 22157</div>
  <svg class="wave" viewBox="0 0 200 40" preserveAspectRatio="none" height="14"><path d="M0 30 Q100 8 200 22 L200 40 L0 40Z" fill="var(--orange)"/><path d="M0 26 Q100 4 200 18" stroke="var(--ink)" stroke-width="3" fill="none"/></svg>
</section>

<section class="sheet env-dl" style="left:876px;top:214px;height:72px">
  <svg viewBox="0 0 314 72" width="314" height="72" style="position:absolute;left:0;top:0">
    <path d="M0 0 L157 40 L314 0" stroke="#d9d9d9" stroke-width="1" fill="none"/>
  </svg>
</section>

</body>
</html>
```